Design mobile friendly review and ranking site

We're working on a corporate website for reviewing and ranking fellow employees. We need the website to look both fun and professional and it needs to be responsive - to it works on mobile and desktop.

Looking for css and HTML for 3 key pages as well as a header and footer for the site. Also would need any supporting graphics as part of the design.

Target Market(s)

Professionals in their 20s, 30s, and 40s.

Industry/Entity Type

Internet

Coding

Coded - Design and coding required

Number of Pages Required

3 page

Font styles to use
Sans Serif

Requirements
Must have
• 3 key pages we need (note included screenshots for each - these are just super rough cuts so you see examples of the content.)
• a) main-intro: A compelling into page with a login/registration form. Should be sleek/modern/enticing. Also we would show the ranking for the top 3 people to tease people re: content.
• b) main-page: Has two sections: One at the top where you would rate someone and one at the bottom where it shows a ranking of people.
• c) profile page: This is where you view a specific person. You see the person's picture, some info about the person, you see their overall rating, you can rate them, and you also see their historical ratings.
Nice to have
• Note we need css and HTML for this. It should feel as sleek and modern. Note also must be responsive design so it works well in mobile and desktop.

```html
<!DOCTYPE html>
<html lang="en">
<head>
<meta charset="utf-8">
<title>PeerPeak – Rank Your Colleagues</title>
<link href="https://fonts.googleapis.com/css2?family=Montserrat:wght@400;600;700&family=Open+Sans:wght@400;600&display=swap" rel="stylesheet">
<style>
:root{
  --blue:#1fa8e8;
  --blue-dark:#1490cc;
  --blue-light:#3cc0f5;
  --orange:#f7a11a;
  --white:#ffffff;
  --text:#6b6b6b;
  --dark:#2b2b2b;
  --darker:#1c1c1c;
  --grey:#9a9a9a;
}
*{box-sizing:border-box;margin:0;padding:0}
html,body{width:768px;height:1200px;overflow:hidden}
body{font-family:"Open Sans",Arial,sans-serif;color:var(--text);background:var(--white)}
.page{position:relative;width:768px;height:1200px}

/* hero */
.hero{position:relative;height:371px;overflow:hidden}
.hero-photo{position:absolute;inset:0;background:
  radial-gradient(ellipse at 30% 85%,#e8b898 0%,rgba(232,184,152,0) 38%),
  radial-gradient(ellipse at 75% 80%,#d9a07d 0%,rgba(217,160,125,0) 40%),
  radial-gradient(ellipse at 88% 30%,#c98a6a 0%,rgba(201,138,106,0) 30%),
  linear-gradient(180deg,#7fa9cf 0%,#b9d3ea 45%,#e6d3c4 100%)}
.hero-shade{position:absolute;inset:0;background:linear-gradient(180deg,rgba(20,40,70,.35),rgba(20,40,70,.05) 60%)}
.topbar{position:absolute;top:0;left:0;right:0;height:58px;display:flex;align-items:center;padding:0 40px}
.brand{font-family:"Montserrat",Arial,sans-serif;font-weight:700;font-size:17px;color:var(--white);letter-spacing:.5px}
.nav{margin-left:auto;display:flex;gap:20px;align-items:center}
.nav a{font-family:"Montserrat",Arial,sans-serif;font-size:9px;color:var(--white);text-decoration:none;letter-spacing:1px}
.nav .btn{margin-left:8px;padding:8px 20px;font-size:10px;font-weight:600}
.btn-outline{border:1px solid var(--white)}
.btn-blue{background:var(--blue)}
.hero-title{position:absolute;top:150px;left:0;right:0;text-align:center;font-family:"Montserrat",Arial,sans-serif;font-weight:600;font-size:15px;line-height:20px;letter-spacing:2px;color:var(--white)}
.tabs{position:absolute;top:202px;left:282px;display:flex}
.tab{width:80px;height:24px;line-height:24px;text-align:center;font-family:"Montserrat",Arial,sans-serif;font-size:9px;font-weight:600;color:var(--white);letter-spacing:1px;background:rgba(255,255,255,.15)}
.tab.active{background:var(--orange)}
.signup{position:absolute;top:232px;left:192px;width:372px;height:38px;background:var(--white);display:flex;align-items:center;padding:4px}
.signup-input{flex:1;font-size:10px;color:var(--grey);padding-left:10px}
.signup-btn{height:28px;width:90px;background:var(--blue);color:var(--white);font-family:"Montserrat",Arial,sans-serif;font-size:9px;font-weight:600;letter-spacing:1px;text-align:center;line-height:28px}

/* welcome */
.welcome{height:162px;text-align:center;padding-top:30px}
.welcome h2{font-family:"Montserrat",Arial,sans-serif;font-weight:400;font-size:20px;color:var(--orange);letter-spacing:1px}
.rule{width:46px;height:2px;background:var(--orange);margin:8px auto 12px}
.welcome p{width:560px;margin:0 auto;font-size:9px;line-height:14px;color:var(--grey)}

/* filter band */
.filter{height:35px;background:var(--orange);display:flex;align-items:center;justify-content:center;gap:14px}
.select{width:92px;height:22px;background:#e58d0c;color:var(--white);font-family:"Montserrat",Arial,sans-serif;font-size:9px;font-weight:600;display:flex;align-items:center;justify-content:space-between;padding:0 10px}
.filter span{font-family:"Montserrat",Arial,sans-serif;font-size:10px;font-weight:600;color:var(--white);letter-spacing:1px}

/* featured */
.featured{position:relative;height:256px;background:var(--blue-light);text-align:center;color:var(--white)}
.avatar{position:absolute;top:22px;left:324px;width:120px;height:120px;border-radius:50%;border:4px solid var(--white);background:radial-gradient(circle at 50% 40%,#6a6a6a,#1e1e1e 70%)}
.person-role{position:absolute;top:150px;left:0;right:0;font-size:9px;margin-left:-120px}
.person-name{position:absolute;top:158px;left:0;right:0;font-family:"Montserrat",Arial,sans-serif;font-weight:400;font-size:34px}
.learn{position:absolute;top:206px;left:339px;width:90px;height:22px;line-height:22px;background:var(--white);color:var(--blue);font-family:"Montserrat",Arial,sans-serif;font-size:8px;font-weight:700;letter-spacing:1px}
.arrow{position:absolute;top:112px}
.arrow.left{left:50px}.arrow.right{right:50px}

/* stats */
.stats{height:67px;display:flex}
.stat{flex:1;display:flex;flex-direction:column;align-items:center;justify-content:center;color:var(--white);background:var(--blue)}
.stat:nth-child(2),.stat:nth-child(4){background:var(--blue-dark)}
.stat:first-child{background:var(--blue-light)}
.stat-value{font-family:"Montserrat",Arial,sans-serif;font-size:24px;line-height:28px}
.stars{font-size:15px;letter-spacing:3px;color:var(--orange);line-height:28px}
.stat-label{font-family:"Montserrat",Arial,sans-serif;font-size:7px;letter-spacing:1px;margin-top:4px}

/* more */
.more{height:146px;background:var(--dark);text-align:center;padding-top:48px}
.more h3{font-family:"Montserrat",Arial,sans-serif;font-weight:700;font-size:19px;letter-spacing:3px;color:var(--white)}
.more p{margin-top:10px;font-size:11px;color:var(--grey)}
.more .hl{color:var(--orange)}.more .wh{color:var(--white)}

/* footer */
.footer{height:163px;background:var(--darker);text-align:center;padding-top:26px}
.footer .brand{font-size:18px}
.tagline{font-size:7px;color:var(--grey);letter-spacing:2px;margin-top:4px}
.footer-nav{margin-top:18px;display:flex;justify-content:center;gap:22px}
.footer-nav a{font-family:"Montserrat",Arial,sans-serif;font-size:7px;color:var(--grey);letter-spacing:1px;text-decoration:none}
.social{margin-top:16px;display:flex;justify-content:center;gap:10px}
.social i{width:20px;height:20px;border-radius:50%;border:1px solid var(--grey)}
</style>
</head>
<body>
<div class="page">
  <header class="hero">
    <div class="hero-photo" role="img" aria-label="Group of smiling colleagues leaning together against a bright sky"></div>
    <div class="hero-shade"></div>
    <div class="topbar">
      <div class="brand">PeerPeak</div>
      <nav class="nav">
        <a href="#">HOW IT WORKS</a>
        <a href="#">ABOUT US</a>
        <a href="#">CONTACT</a>
        <a href="#" class="btn btn-outline">REGISTER</a>
        <a href="#" class="btn btn-blue">LOG IN</a>
      </nav>
    </div>
    <h1 class="hero-title">TO SEE HOW PEOPLE ARE RANKED IN YOUR<br>COMPANY LOGIN OR REGISTER BELOW</h1>
    <div class="tabs"><div class="tab active">REGISTER</div><div class="tab">LOGIN</div></div>
    <div class="signup"><div class="signup-input">Your Work Email</div><div class="signup-btn">REGISTER</div></div>
  </header>

  <section class="welcome">
    <h2>WELCOME</h2>
    <div class="rule"></div>
    <p>PeerPeak helps teams see how colleagues are valued across the company. Share honest reviews, rate the people you work with every day, and discover who leads in skill, teamwork and effort. Rankings refresh weekly, so every contribution counts and great work never goes unnoticed by the people who matter most in your office.</p>
  </section>

  <section class="filter">
    <div class="select">BEST <svg width="8" height="6" viewBox="0 0 8 6"><path d="M0 0h8L4 6z" fill="#fff"/></svg></div>
    <span>PEOPLE</span>
  </section>

  <section class="featured">
    <svg class="arrow left" width="12" height="20" viewBox="0 0 12 20"><path d="M10 2 2 10l8 8" fill="none" stroke="#fff" stroke-width="2.5"/></svg>
    <div class="avatar" role="img" aria-label="Portrait photo of the featured colleague"></div>
    <div class="person-role">Sales Lead</div>
    <div class="person-name">Dan Mercer</div>
    <div class="learn">LEARN MORE</div>
    <svg class="arrow right" width="12" height="20" viewBox="0 0 12 20"><path d="M2 2l8 8-8 8" fill="none" stroke="#fff" stroke-width="2.5"/></svg>
  </section>

  <section class="stats">
    <div class="stat"><div class="stat-value">15</div><div class="stat-label">STARS</div></div>
    <div class="stat"><div class="stat-value">1</div><div class="stat-label">NUMBER OF REVIEWS</div></div>
    <div class="stat"><div class="stars">★★★★★</div><div class="stat-label">SMARTS</div></div>
    <div class="stat"><div class="stars">★★★★★</div><div class="stat-label">EASY TO WORK WITH</div></div>
    <div class="stat"><div class="stars">★★★★★</div><div class="stat-label">HARD WORKER</div></div>
  </section>

  <section class="more">
    <h3>WANT TO SEE MORE RANKINGS?</h3>
    <p><span class="hl">Login</span> or <span class="wh">register</span> below</p>
  </section>

  <footer class="footer">
    <div class="brand">PeerPeak</div>
    <div class="tagline">COMPANY RANKINGS</div>
    <nav class="footer-nav">
      <a href="#">TOP RANKINGS</a><a href="#">HOW IT WORKS</a><a href="#">LEARN MORE</a><a href="#">CONTACT US</a>
    </nav>
    <div class="social"><i></i><i></i><i></i><i></i></div>
  </footer>
</div>
</body>
</html>
```